Beauty Salon Industry - Web Design Project

zQuarta is a well-funded start up developing an Online Marketing Platform for small businesses in Europe.
We require a large number of high quality business web designs for our business website builder. Our business websites are seamlessly integrated into our Online Marketing systems and therefore it is important for designers to comply with our Design Guidelines.
This is our second contest and it will focus on the beauty salon industry. We will be running contents every 2-3 weeks for a new industry. Last month, we ran a contest for Builder website designs with 3 top prizes (plus £10 per variation) and we also paid out £25 per design for 20+ entries from designers who did not win the top prizes. So we encourage all entries!
We have included a wire frame this time to encourage you to be as creative as possible with your designs and layout while respecting the following guidelines:
1) You CAN change the layout as much as you like. If you think a vertical menu would look better, then use it. If you think the design would benefit from moving an element to a different location, then you can do that too.
2) You must include ALL the elements in the wire frame in your design.(e.g. latest 2 news entries, a testimonial, 1 gallery image, carousel etc...). Please make sure you have looked through the wire frame and know what is required. Entries that do not include all the elements will not qualify to win.
3) So remember, you CAN change the layout as much as you like but DO NOT remove any elements nor move them to a different page.
4) You may change the size and style of the carousel image. We would like to see as many variations of this as possible.
We are rewarding 3 prizes, and would like the winning designer to design the internal pages to the new design.
As always, if we think your designs could be incorporated into our system, but you do not win the competition, we will reward £25. Therefore, we encourage designers to submit as many designs as possible as we may award up to 25 designs.
Judging criteria : -
1) Visual Design
2) Layout must adhere to best practices and wireframe. If you decide to move elements around significantly please provide reason
3) Functional, informative and drives calls to action
Updates
As usual:
1st place = £350
2nd place = £250
3rd place = £150
Good luck!
Very happy with all the designs submitted so far, and will provide feedback ASAP.
We would like to see you try arranging the elements differently. So please try different navigation types and layouts.
Thanks
Morris
Prize funds for 1st place has been slightly increased.
Thanks
Morris
We have already had some amazing designs submitted. Thanks.
Remember to play with the layout of the elements and try designs with a carousel/slider that is in portrait not just in landscape.
Thanks everyone!
Morris
Hi everyone, we are really enjoying looking through the designs.
We have one NEW requirement. If you have used an image from http://www.frelik-example.com/ in your design, could you please replace it with another.
We are not associated with them.
Thank you.
I have just sent a poll around the office to vote on all the designs and hope to have the results soon.
Good luck and I hope to see all your great designs for our next project in a couple of weeks.
Morris
Hi everyone, we hope you have had a good holiday season. We will be rewarding the prizes very soon, hopefully today or tomorrow.
Thanks
Morris
We are currently going through all the designs that did not win our competition and will be contacting the designers of the designs we would like to use in our system, so please keep an eye on your inbox over the next few days.
Thank you
Morris
Target Market(s)
Beauty Salon Industry
Industry/Entity Type
Beauty Salon
Look and feel
Each slider illustrates characteristics of the customer's brand and the style your logo design should communicate.

```html
<!DOCTYPE html>
<html lang="en">
<head>
<meta charset="utf-8">
<title>Loft Lather – Hair and Urban Spa</title>
<link rel="stylesheet" href="https://fonts.googleapis.com/css2?family=Lato:wght@300;400;700&display=swap">
<style>
:root{
  --page-dark:#201c1a;
  --ink:#4a4848;
  --ink-soft:#8a8888;
  --ink-mid:#5c5a5a;
  --nav-bg:#0c0c0c;
  --white:#ffffff;
  --rule:#c9c9c9;
  --btn-dark:#545353;
  --frame:#5b5655;
  --hair:#5e3b2a;
}
*{box-sizing:border-box;margin:0;padding:0}
html,body{width:1200px;height:960px;overflow:hidden}
body{position:relative;background:var(--page-dark);font-family:"Lato",Arial,sans-serif;color:var(--ink)}
.abs{position:absolute}
.page-band{left:0;top:147px;width:1200px;height:641px;background:var(--white);border-bottom:5px solid #d8d8d8}
.header{left:136px;top:9px;width:928px;height:96px;background:linear-gradient(180deg,#eeeeee 0%,#d6d6d6 60%,#bdbdbd 100%)}
.brand-mark{left:161px;top:25px;width:60px;height:60px;background:#8d8d8d;border-radius:4px}
.brand-name{left:240px;top:20px;font-weight:300;font-size:44px;color:var(--white);letter-spacing:.5px;line-height:1}
.brand-tag{left:242px;top:67px;font-size:15px;color:var(--white);font-weight:400}
.phone{left:740px;top:33px;font-size:26px;font-weight:300;color:var(--white);z-index:3}
.btn-dark{background:var(--btn-dark);color:var(--white);border:1px solid #e5e5e5;font-weight:400;display:flex;align-items:center;justify-content:center;z-index:3}
.book-now{left:817px;top:65px;width:94px;height:26px;font-size:17px}
.nav{left:136px;top:105px;width:928px;height:42px;background:var(--nav-bg)}
.nav a{position:absolute;color:#cfcfcf;font-size:17px;text-decoration:none;top:11px}
.nav a.current{color:var(--white)}
.hero-photo{left:952px;top:28px;width:108px;height:284px;z-index:1;border-radius:45% 45% 20% 20%/25% 25% 8% 8%;background:linear-gradient(180deg,#e8c7b0 0%,#7a4d35 30%,var(--hair) 75%,rgba(94,59,42,0) 100%)}
.panel{background:linear-gradient(90deg,#ffffff 0%,#f3f3f3 70%,#e2e2e2 100%)}
.intro-panel{left:145px;top:150px;width:228px;height:335px}
.intro-title{left:151px;top:180px;font-size:23px;font-weight:400;color:var(--ink);line-height:27px;text-transform:uppercase}
.intro-text{left:154px;top:276px;width:180px;font-family:Arial,sans-serif;font-size:11.5px;line-height:13.6px;color:#333}
.intro-text p+p{margin-top:8px}
.btn-light{background:linear-gradient(#ffffff,#ededed);border:1px solid #cfcfcf;color:#6b6b6b;font-size:11.5px;font-family:Arial,sans-serif;display:flex;align-items:center;justify-content:center}
.rule{height:2px;background:var(--rule)}
.gallery-photo{left:155px;top:506px;width:192px;height:227px;border:1px solid #bdbdbd;background:linear-gradient(135deg,#d9d9d9 0%,#8c6a5c 45%,#5a3a2d 75%,#b7b7b7 100%)}
.center-panel{left:375px;top:150px;width:448px;height:335px;background:linear-gradient(180deg,#e2e2e2,#f8f8f8 50%,#e6e6e6)}
.slider{left:459px;top:147px;width:282px;height:373px;background:var(--frame);box-shadow:0 6px 8px rgba(0,0,0,.25)}
.slide-photo{left:468px;top:157px;width:263px;height:315px;background:radial-gradient(ellipse at 55% 40%,#c4a089 0%,#8b5a3f 35%,#6c6b6c 70%,#4a4a4a 100%)}
.dot{top:491px;width:13px;height:13px;background:#7b7675}
.dot.on{background:#dedede}
.quote{left:389px;top:542px;width:430px;font-size:13px;line-height:16px;color:#666}
.quote-name{left:392px;top:584px;font-size:13.5px;color:#6a6a6a}
.news-box{left:375px;top:622px;width:448px;height:151px;background:#eeeeee;border:1px solid #d6d6d6}
.news-item{width:172px}
.news-date{font-size:11.5px;color:#777}
.news-title{font-size:15px;color:#555;margin-top:3px;font-weight:400;white-space:nowrap}
.news-body{font-size:11px;line-height:17px;color:#999;margin-top:6px}
.offer-panel{left:825px;top:150px;width:239px;height:244px}
.offer-price{left:861px;top:204px;font-size:46px;font-weight:700;color:var(--ink-mid);line-height:1;z-index:2}
.offer-text{left:861px;top:262px;font-size:15px;font-weight:700;color:var(--ink-mid);line-height:18px;z-index:2}
.book-appt{left:856px;top:331px;width:191px;height:27px;font-size:15px}
.side-title{font-size:15px;color:var(--ink-mid);font-weight:700}
.address{left:861px;top:444px;font-size:13px;line-height:19.5px;color:#8a8a8a}
.hours{left:861px;top:622px;font-size:13px;color:#555;border-collapse:collapse}
.hours td{height:19.7px;padding:0}
.hours td.day{color:#9a9a9a;width:38px}
.partners{left:136px;top:795px;width:928px;height:112px;background:linear-gradient(180deg,#e4e4e4,#ffffff 25%,#ffffff 75%,#dedede)}
.partner{top:838px;font-size:26px;color:#2b2b2b;transform:translateX(-50%);white-space:nowrap}
.footer{left:823px;top:909px;width:241px;height:27px;background:#4b4847}
.footer-text{left:836px;top:916px;font-size:11px;color:#e0e0e0;font-family:Arial,sans-serif}
.admin{left:1011px;top:913px;width:45px;height:19px;background:#676361;border:1px solid #888;color:#eee;font-size:11px;font-family:Arial,sans-serif;display:flex;align-items:center;justify-content:center}
</style>
</head>
<body>
<div class="abs page-band"></div>

<header>
  <div class="abs header"></div>
  <div class="abs brand-mark"></div>
  <div class="abs brand-name">LOFT LATHER</div>
  <div class="abs brand-tag">Hair and Urban Spa</div>
  <div class="abs phone">020 7946 0181</div>
  <div class="abs btn-dark book-now">Book Now</div>
  <nav class="abs nav">
    <a class="current" style="left:22px">Home</a>
    <a style="left:96px">Services</a>
    <a style="left:186px">Gallery</a>
    <a style="left:268px">Testimonials</a>
    <a style="left:389px">News</a>
    <a style="left:459px">About Us</a>
    <a style="left:556px">Contact Us</a>
  </nav>
</header>

<section class="intro">
  <div class="abs panel intro-panel"></div>
  <h1 class="abs intro-title">Let our hair and<br>beauty skills<br>blow you away</h1>
  <div class="abs intro-text">
    <p>Loft Lather is a passionate, creative team, dedicated to delivering a second to none, personal salon experience that will 'blow' your mind.</p>
    <p>Where ultimate hairdressing comes hand-in-hand with style, glamour, fashion, innovation and skill to create an exquisite salon experience in theheart of London</p>
  </div>
  <div class="abs btn-light" style="left:270px;top:443px;width:78px;height:20px">Read More</div>
  <div class="abs rule" style="left:146px;top:484px;width:216px"></div>
  <div class="abs gallery-photo" role="img" aria-label="Gallery photo of a woman with long straight brown hair"></div>
  <div class="abs btn-light" style="left:267px;top:748px;width:78px;height:21px">View More</div>
</section>

<section class="carousel">
  <div class="abs center-panel"></div>
  <svg class="abs" style="left:410px;top:296px" width="20" height="36" viewBox="0 0 20 36"><polyline points="17,2 3,18 17,34" fill="none" stroke="#9a9a9a" stroke-width="1.5"/></svg>
  <svg class="abs" style="left:765px;top:296px" width="20" height="36" viewBox="0 0 20 36"><polyline points="3,2 17,18 3,34" fill="none" stroke="#9a9a9a" stroke-width="1.5"/></svg>
  <div class="abs slider"></div>
  <div class="abs slide-photo" role="img" aria-label="Carousel photo of a woman with a short auburn bob being styled with scissors"></div>
  <div class="abs dot on" style="left:486px"></div>
  <div class="abs dot" style="left:513px"></div>
  <div class="abs dot" style="left:539px"></div>
  <div class="abs dot" style="left:566px"></div>
  <div class="abs dot" style="left:593px"></div>
  <div class="abs dot" style="left:619px"></div>
  <div class="abs dot" style="left:646px"></div>
  <div class="abs dot" style="left:673px"></div>
  <div class="abs dot" style="left:699px"></div>
</section>

<section class="testimonial">
  <p class="abs quote">"My hairstylist, annika, was truly amazing. She listened to exactly what I wanted, but also told me exactly what ..."</p>
  <p class="abs quote-name">Mirela Osten</p>
  <div class="abs btn-light" style="left:736px;top:583px;width:75px;height:20px">Read More</div>
</section>

<section class="news">
  <div class="abs news-box"></div>
  <article class="abs news-item" style="left:387px;top:633px">
    <div class="news-date">1 dec 2011</div>
    <h3 class="news-title">Book Now For Christmas</h3>
    <p class="news-body">Our salon is usually very busy for the two weeks before Christmas, so please book early: call 020 7946 0181, or contact us.</p>
  </article>
  <article class="abs news-item" style="left:612px;top:633px">
    <div class="news-date">9 nov 2011</div>
    <h3 class="news-title">Want to be hair model?</h3>
    <p class="news-body">We always need models for our portfolio. If you want to become one please contact us.</p>
  </article>
  <div class="abs btn-light" style="left:733px;top:745px;width:78px;height:21px">More News</div>
</section>

<aside class="sidebar">
  <div class="abs panel offer-panel"></div>
  <div class="abs hero-photo" role="img" aria-label="Photo of a woman with very long straight brown hair"></div>
  <div class="abs offer-price">£25</div>
  <div class="abs offer-text">Complimentary<br>gift for first-time<br>clients!</div>
  <div class="abs btn-dark book-appt">Book Appointment Now</div>
  <div class="abs rule" style="left:837px;top:397px;width:216px"></div>
  <h2 class="abs side-title" style="left:861px;top:418px">LOFT LATHER</h2>
  <div class="abs address">12 Larkin Mews<br>London<br>W9X 2QT</div>
  <div class="abs btn-light" style="left:856px;top:518px;width:78px;height:21px">View Map</div>
  <div class="abs rule" style="left:837px;top:566px;width:216px"></div>
  <h2 class="abs side-title" style="left:861px;top:588px">Business Hours</h2>
  <table class="abs hours">
    <tr><td class="day">Mon.</td><td>9 a.m - 5 p.m.</td></tr>
    <tr><td class="day">Tue.</td><td>9 a.m - 5 p.m.</td></tr>
    <tr><td class="day">Wed.</td><td>9 a.m - 5 p.m.</td></tr>
    <tr><td class="day">Thu.</td><td>9 a.m - 5 p.m.</td></tr>
    <tr><td class="day">Fri.</td><td>9 a.m - 5 p.m.</td></tr>
    <tr><td class="day">Sat.</td><td>9 a.m - 5 p.m.</td></tr>
  </table>
</aside>

<footer>
  <div class="abs partners"></div>
  <div class="abs partner" style="left:253px">Verane</div>
  <div class="abs partner" style="left:488px">Solvio</div>
  <div class="abs partner" style="left:725px">Pell and Pine</div>
  <div class="abs partner" style="left:956px">Haldermann</div>
  <div class="abs footer"></div>
  <div class="abs footer-text">Managed by zQuarta.com</div>
  <div class="abs admin">Admin</div>
</footer>
</body>
</html>
```